New Business Card/Website Logo

We need a business card design for a new company based in Sydney. The company focuses mainly in construction in the field of form work and concreting. Attached is the logo being used already which can be used as a base for a new design, the current one is simply too bland and we are looking to spruce it up so it stands out and looks nicer. The logo would also be used on the website which is currently under construction. The attached image has the name, mobile and also the license number which needs to be there. The current email address on there can be removed and can be replaced with the website http://www.bravelintel.com.au, thanks!
Updates

Target Market(s)

Construction industry. Focusing on form work and concreting

Industry/Entity Type

Construction

Requirements
Must have
• License # on card along with website http://www.bravelintel.com.au and mobile phone number
Nice to have
• You have freedom with the design. The current design was a mock up done quite quickly. Please just keep in mind the target audience - construction, thanks.
Should not have
• the mailvista email address can be removed(refer picture) and replaced somewhere on the design with the website http://www.bravelintel.com.au

```html
<!DOCTYPE html>
<html lang="en">
<head>
<meta charset="utf-8">
<title>Bravel Intel – Business Card</title>
<link rel="stylesheet" href="https://fonts.googleapis.com/css2?family=Arimo:wght@400;700&display=swap">
<style>
  :root {
    --backdrop: #2b2d2f;
    --paper: #ffffff;
    --brand-green: #4f9a3a;
    --band-green: #5a9a43;
    --band-green-deep: #4a8535;
    --ink-grey: #4a4a4a;
    --ink-white: #ffffff;
  }
  * { box-sizing: border-box; margin: 0; padding: 0; }
  html, body { width: 1200px; height: 790px; overflow: hidden; }
  body {
    background: var(--backdrop);
    font-family: "Arimo", Arial, sans-serif;
    position: relative;
  }

  .business-card {
    position: absolute;
    left: 420px; top: 70px;
    width: 700px; height: 400px;
    background: var(--paper);
    box-shadow: 0 12px 30px rgba(0,0,0,.45);
  }
  .card-brand {
    position: absolute;
    left: 0; right: 0; top: 0; height: 160px;
    display: flex; align-items: center; justify-content: center; gap: 14px;
  }
  .brand-square {
    width: 34px; height: 34px; background: var(--brand-green); flex: none;
  }
  .brand-name {
    font-weight: 700; font-size: 46px; letter-spacing: 2px;
    color: var(--ink-grey);
    white-space: nowrap;
  }
  .card-band {
    position: absolute;
    left: 0; right: 0; top: 160px; height: 200px;
    background: var(--band-green);
    color: var(--ink-white);
  }
  .band-scene {
    position: absolute; right: 0; top: 0; width: 58%; height: 100%;
    background: linear-gradient(90deg, var(--band-green) 0%, var(--band-green-deep) 55%, var(--band-green) 100%);
    opacity: .85;
  }
  .holder-name {
    position: absolute; left: 40px; top: 28px;
    font-weight: 700; font-size: 26px; letter-spacing: .5px;
  }
  .licence {
    position: absolute; right: 36px; top: 30px;
    font-size: 15px;
  }
  .contact-list {
    position: absolute; left: 40px; top: 104px;
    list-style: none;
  }
  .contact-list li {
    display: flex; align-items: center; gap: 10px;
    font-size: 17px; line-height: 30px;
    white-space: nowrap;
  }
  .contact-list .phone { font-weight: 700; font-size: 20px; }
  .contact-list svg { width: 16px; height: 16px; flex: none; }

  .logo-panel {
    position: absolute;
    left: 4px; top: 575px;
    width: 428px; height: 210px;
    background: var(--paper);
    display: flex; align-items: center; justify-content: center; gap: 14px;
  }
  .logo-panel .brand-square { width: 30px; height: 30px; }
  .logo-panel .brand-name { font-size: 40px; letter-spacing: 1px; }
</style>
</head>
<body>

<section class="business-card">
  <header class="card-brand">
    <span class="brand-square"></span>
    <span class="brand-name">BRAVEL INTEL</span>
  </header>

  <div class="card-band">
    <div class="band-scene" role="img" aria-label="Faint photo of construction workers on a formwork site with scaffolding"></div>
    <h1 class="holder-name">Marco Delgado</h1>
    <p class="licence">Licence No. 480392B</p>
    <ul class="contact-list">
      <li class="phone">
        <svg viewBox="0 0 16 16" aria-hidden="true"><path fill="#fff" d="M3.6 1.2l2.2 2.6-1.3 1.6c.9 2.1 2.4 3.6 4.5 4.5l1.6-1.3 2.6 2.2-1.4 2.2C7 12.6 3.4 9 1.4 2.6z"/></svg>
        0400 555 019
      </li>
      <li>
        <svg viewBox="0 0 16 16" aria-hidden="true"><circle cx="8" cy="8" r="6.5" fill="none" stroke="#fff" stroke-width="1.3"/><ellipse cx="8" cy="8" rx="2.8" ry="6.5" fill="none" stroke="#fff" stroke-width="1.1"/><path d="M1.5 8h13" stroke="#fff" stroke-width="1.1"/></svg>
        www.bravelintel.com.au
      </li>
    </ul>
  </div>
</section>

<section class="logo-panel">
  <span class="brand-square"></span>
  <span class="brand-name">BRAVEL INTEL</span>
</section>

</body>
</html>
```